create clean, simple business card template

using the logo created now we need to create a simple, elegant business card design to suit

Industry/Entity Type

Business

Font styles to use
Other font styles liked:
• segoe ui

Requirements
Must have
• Front:
"Name:"
"Title:"
"Mobile:"
"email:"
and the logo

Back:
Logo
Nice to have
• Text in black but other graphics etc to match colours in logo as provided

```html
<!DOCTYPE html>
<html lang="en">
<head>
<meta charset="utf-8">
<title>Halden Estates – Business Card</title>
<link href="https://fonts.googleapis.com/css2?family=Open+Sans:wght@400;600&display=swap" rel="stylesheet">
<style>
  :root {
    --backdrop: #3b8099;
    --card: #ffffff;
    --card-edge: #e4e4e4;
    --bronze: #7b6339;
    --espresso: #352d26;
    --ink: #3a3a3a;
  }
  * { margin: 0; padding: 0; box-sizing: border-box; }
  html, body {
    width: 1200px; height: 1200px; overflow: hidden;
    background: var(--backdrop);
    font-family: "Open Sans", "Segoe UI", sans-serif;
  }
  .card {
    position: absolute; left: 323px; width: 555px; height: 308px;
    background: radial-gradient(ellipse at center, var(--card) 55%, var(--card-edge) 100%);
    overflow: hidden;
  }
  .card--front { top: 240px; }
  .card--back { top: 681px; }

  .accent-bronze { position: absolute; left: 0; top: 38px; width: 50px; height: 247px; background: var(--bronze); }
  .accent-gap { position: absolute; left: 0; top: 78px; width: 28px; height: 230px; background: var(--card); }
  .accent-dark { position: absolute; left: 0; top: 81px; width: 22px; height: 227px; background: var(--espresso); }

  .brand {
    position: absolute; left: 0; right: 0;
    display: flex; align-items: center; justify-content: center; gap: 12px;
    color: var(--bronze); font-weight: 600; white-space: nowrap;
  }
  .brand__dot { border-radius: 50%; background: var(--bronze); flex: none; }
  .card--front .brand { top: 40px; font-size: 34px; }
  .card--front .brand__dot { width: 22px; height: 22px; }
  .card--back .brand { top: 118px; font-size: 44px; }
  .card--back .brand__dot { width: 28px; height: 28px; }

  .person { position: absolute; left: 0; right: 0; top: 134px; text-align: center; color: var(--ink); }
  .person__name { font-size: 28px; line-height: 36px; font-weight: 400; }
  .person__title { font-size: 18px; line-height: 22px; }

  .contact { position: absolute; left: 0; right: 0; top: 236px; text-align: center; color: var(--bronze); font-size: 18px; line-height: 28px; }
</style>
</head>
<body>
  <section class="card card--front">
    <div class="accent-bronze"></div>
    <div class="accent-gap"></div>
    <div class="accent-dark"></div>
    <div class="brand"><span class="brand__dot"></span>Halden Estates</div>
    <div class="person">
      <p class="person__name">Full Name</p>
      <p class="person__title">Tittle</p>
    </div>
    <div class="contact">
      <p>Mobile: 712 480 365</p>
      <p>Email: contact@haldenestates.com</p>
    </div>
  </section>

  <section class="card card--back">
    <div class="brand"><span class="brand__dot"></span>Halden Estates</div>
  </section>
</body>
</html>
```